Flyer for Compassion training days

I need a A5-size, single-sided flyer design for my training days. They are weekends in a blend of Compassionate Communication and Buddhist teachings called Palomere Communication. The logo for Palomere that should be included.
The flyer needs room for 1) course title, 2) course dates, location & price, 3) course description, 4) booking info, 5) my picture & short bio, and 6) the palomere.co website (yes, it is 'co' and not 'com).
Updates

Target Market(s)

Women 35-65 years, well-educated, spiritually minded. May have interests like yoga and meditation.

Industry/Entity Type

Health And Wellness

Font styles to use
Sans Serif
Other font styles liked:
• Blue Plaque, Josefina are both great

Colors
fbf289
fdf9cf
cfeae6
33b8a4

Requirements
Must have
• The Palomere logo; my picture.
• Elegance. Calm and expansive feel.
• The poster provided in the project files shows you the kind of information I need to include.
• Colours -- greens and yellows, but the options on pixel harbor are not quite the right shades.
• The logo colour can be changed.
Nice to have
• Classy (but not cliche) image associated with Buddhism; gentle curves similar to those on the business card (see project files).
Should not have
• Dark background. Busy, loud design. Overly 'swirly' design. Images that I have to buy separately.

```html
<!DOCTYPE html>
<html lang="en">
<head>
<meta charset="utf-8">
<title>Palomere Communication Core Course Flyer</title>
<link rel="stylesheet" href="https://fonts.googleapis.com/css2?family=Crimson+Pro:ital,wght@0,700;1,600;1,700&family=Roboto+Condensed:wght@400;700&family=Source+Sans+3:ital,wght@0,400;0,700;1,400;1,600&display=swap">
<style>
  :root {
    --page-bg: #e9ebe6;
    --green: #39b54a;
    --green-deep: #1f9a3a;
    --green-text: #17923c;
    --lime: #b8e25a;
    --lime-pale: #eef8c8;
    --ink: #141414;
    --body: #2a2a2a;
    --gold: #b9852e;
    --gold-light: #e3b765;
    --sepia: #9b8a62;
    --white: #ffffff;
  }
  * { margin: 0; padding: 0; box-sizing: border-box; }
  html, body { width: 1061px; height: 1200px; overflow: hidden; background: var(--page-bg); }
  .flyer {
    position: absolute; left: 117px; top: 19px;
    width: 918px; height: 1290px;
    transform: scale(0.9); transform-origin: top left;
    background: var(--white); overflow: hidden;
    box-shadow: 0 6px 24px rgba(0,0,0,.18);
    font-family: "Source Sans 3", sans-serif; color: var(--body);
  }
  .backdrop { position: absolute; inset: 0; }
  .abs { position: absolute; }

  .title-panel {
    left: 42px; top: 27px; width: 468px; height: 380px;
    background: linear-gradient(180deg, rgba(255,255,255,.85), rgba(255,255,255,.35) 80%, rgba(255,255,255,0));
  }
  .title-lead { left: 92px; top: 40px; font-family: "Source Sans 3", sans-serif; font-weight: 700; font-size: 31px; color: var(--green-text); }
  .title-mid { left: 92px; top: 74px; font-family: "Roboto Condensed", sans-serif; font-size: 29px; color: var(--ink); }
  .title-course { left: 92px; top: 112px; font-family: "Roboto Condensed", sans-serif; font-weight: 700; font-size: 24px; color: var(--ink); }
  .dates { left: 86px; top: 146px; font-family: "Crimson Pro", serif; font-weight: 700; font-size: 70px; color: var(--ink); letter-spacing: 1px; }
  .venue { left: 86px; top: 214px; font-family: "Roboto Condensed", sans-serif; font-weight: 700; font-size: 26px; color: var(--ink); }

  .butterfly-art { left: 48px; top: 292px; width: 76px; height: 70px; border-radius: 40%; background: radial-gradient(circle, rgba(150,110,60,.5), rgba(150,110,60,0) 70%); }
  .statue-photo { left: 522px; top: 12px; width: 348px; height: 470px; border-radius: 45% 45% 12% 12%; background: radial-gradient(ellipse at 50% 45%, var(--gold-light), var(--gold) 55%, rgba(185,133,46,0) 78%); }

  .price-badge { left: 262px; top: 268px; width: 210px; height: 210px; }
  .price-text { left: 262px; top: 322px; width: 210px; text-align: center; font-family: "Roboto Condensed", sans-serif; font-weight: 700; font-size: 50px; line-height: 50px; color: var(--white); }

  .brand { left: 30px; top: 500px; display: flex; align-items: center; gap: 12px; }
  .brand-dot { width: 34px; height: 34px; border-radius: 50%; background: var(--green); }
  .brand-name { font-family: "Source Sans 3", sans-serif; font-weight: 700; font-size: 34px; color: var(--green); }

  .intro { left: 248px; top: 520px; width: 620px; font-style: italic; font-size: 19.5px; line-height: 25px; color: var(--body); }

  .pill {
    height: 32px; padding: 0 14px; border-radius: 10px;
    background: linear-gradient(180deg, #9fe07f, var(--green));
    box-shadow: inset 0 0 0 2px rgba(255,255,255,.6);
    font-family: "Crimson Pro", serif; font-style: italic; font-weight: 700; font-size: 24px; line-height: 32px; color: var(--ink);
  }
  .pill-explore { left: 42px; top: 638px; }
  .pill-facilitator { left: 56px; top: 862px; }

  .topics { left: 56px; top: 684px; width: 720px; display: grid; grid-template-columns: 402px 1fr; font-style: italic; font-size: 19.5px; line-height: 25px; list-style: none; }
  .topics li { padding-left: 14px; text-indent: -14px; }
  .topics li::before { content: "* "; color: var(--green); }

  .audience { left: 56px; top: 770px; width: 780px; font-size: 20px; line-height: 25px; }
  .bio { left: 56px; top: 906px; width: 780px; font-size: 20px; line-height: 25px; }

  .portrait-ring { left: 25px; top: 974px; width: 310px; height: 310px; border-radius: 50%; background: #d3ecb9; border: 4px solid #b8df96; }
  .portrait-photo { left: 40px; top: 989px; width: 280px; height: 280px; border-radius: 50%; background: radial-gradient(circle at 50% 40%, #c9bb93, var(--sepia) 70%, #6f6243); border: 3px solid var(--white); }

  .coaching { left: 480px; top: 1030px; width: 440px; text-align: center; font-style: italic; font-weight: 600; font-size: 24px; line-height: 30px; color: var(--green-text); }
  .booking { left: 480px; top: 1104px; width: 440px; text-align: center; font-family: "Crimson Pro", serif; font-style: italic; font-weight: 600; font-size: 25px; line-height: 31px; color: var(--ink); }
  .website { left: 480px; top: 1172px; width: 440px; text-align: center; font-weight: 700; font-size: 34px; color: var(--ink); }
</style>
</head>
<body>
<main class="flyer">
  <svg class="backdrop" width="918" height="1290" viewBox="0 0 918 1290" aria-hidden="true">
    <defs>
      <radialGradient id="sky" cx="70%" cy="15%" r="90%">
        <stop offset="0" stop-color="#fbfbd8"/>
        <stop offset=".45" stop-color="#c9ec72"/>
        <stop offset="1" stop-color="#5cc63a"/>
      </radialGradient>
      <linearGradient id="band" x1="0" x2="1">
        <stop offset="0" stop-color="#2fae3e"/>
        <stop offset=".5" stop-color="#7fd34d"/>
        <stop offset="1" stop-color="#2fae3e"/>
      </linearGradient>
      <linearGradient id="base" x1="0" x2="1" y1="0" y2="1">
        <stop offset="0" stop-color="#3cb848"/>
        <stop offset=".5" stop-color="#9ad84f"/>
        <stop offset="1" stop-color="#22a23b"/>
      </linearGradient>
      <linearGradient id="panel" x1="0" x2="1">
        <stop offset="0" stop-color="#ffffff"/>
        <stop offset="1" stop-color="#ececec"/>
      </linearGradient>
    </defs>
    <rect width="918" height="540" fill="url(#sky)"/>
    <path d="M0,420 C220,400 430,445 600,492 C720,525 840,485 918,440 L918,1290 L0,1290 Z" fill="var(--white)"/>
    <path d="M0,410 C220,390 430,432 600,482 C720,515 840,470 918,428 L918,448 C840,500 720,540 592,508 C430,462 220,420 0,424 Z" fill="url(#band)"/>
    <path d="M0,1130 C150,1118 300,1140 400,1108 C550,1058 750,996 918,990 L918,1290 L0,1290 Z" fill="url(#base)"/>
    <path d="M390,1160 C520,1060 720,1030 918,1055 L918,1172 C800,1232 680,1270 560,1262 C480,1256 420,1222 390,1160 Z" fill="url(#panel)"/>
  </svg>

  <div class="abs title-panel"></div>
  <div class="abs title-lead">Mindfulness + Kindness +</div>
  <div class="abs title-mid">Compassionate Communication =</div>
  <div class="abs title-course">Palomere Communication&nbsp; Core Course</div>
  <div class="abs dates">11-12 Dec</div>
  <div class="abs venue">Harrowfield Centre, Edinburgh</div>

  <div class="abs butterfly-art" role="img" aria-label="Small butterfly illustration"></div>
  <div class="abs statue-photo" role="img" aria-label="Photograph of a golden seated Buddha statue"></div>

  <svg class="abs price-badge" viewBox="0 0 210 210" aria-hidden="true">
    <polygon fill="var(--green)" points="105,0 115,21 131,3 136,26 155,12 155,35 177,26 171,48 194,44 183,65 206,66 191,84 210,95 194,107 210,120 189,128 201,147 178,150 185,172 162,170 163,193 141,185 136,207 118,193 105,210 92,193 74,207 69,185 47,193 48,170 25,172 32,150 9,147 21,128 0,120 16,107 0,95 19,84 4,66 27,65 16,44 39,48 33,26 55,35 55,12 74,26 79,3 95,21"/>
    <circle cx="105" cy="105" r="82" fill="none" stroke="#8fdc7a" stroke-width="2"/>
  </svg>
  <div class="abs price-text">(£125/<br>100)</div>

  <div class="abs brand"><span class="brand-dot"></span><span class="brand-name">Palomere</span></div>

  <p class="abs intro">Palomere Communication can help you increase awareness &amp; compassion in everyday speech (with yourself &amp; others), better understand your own patterns, and build resilience to challenging situations. Choose from:</p>

  <h2 class="abs pill pill-explore">In this 2-day Core Course, we’ll explore:</h2>
  <ul class="abs topics">
    <li>Compassionate Communication;</li>
    <li>mindfulness practices;</li>
    <li>Buddhist teachings on Right Speech, loving-kindness, Right Effort, and more;</li>
    <li>choices available to us in our everyday speech.</li>
  </ul>

  <p class="abs audience">This workshop will be of interest if you’d like to improve personal and/or professional relationships. Open to all, best suited to those with at least 1 year’s experience with Mindfulness, Buddhism, or Compassionate Communication / NVC.</p>

  <h2 class="abs pill pill-facilitator">Facilitator:</h2>
  <p class="abs bio">Maribeth Okonwell is an experienced group facilitator, having worked with a range of organisations and presented at a number of festivals &amp; conferences.</p>

  <div class="abs portrait-ring"></div>
  <div class="abs portrait-photo" role="img" aria-label="Sepia portrait photograph of the facilitator"></div>

  <p class="abs coaching">Maribeth offers coaching in<br>Palomere Communication.</p>
  <p class="abs booking">Booking: Book online at TicketLoom<br>or write maribeth@palomere.co</p>
  <p class="abs website">www.palomere.co</p>
</main>
</body>
</html>
```